Software Company Business Card

We are looking for a new design of our business card. The design will also be used in the rest of our branding and marketing materials as we want to keep it all uniform. We sell POS software to fine/luxury jewelers and also offer other business services as well to help the jeweler manage their business and need something more updated, technical and fresh, preferably more on the masculine side. We do not want any designs with gems in them but if possible would like to incorporate the circle and arrow in the logo into the design, but not a requirement if you can't make it work. I would like to see a variety of the mix. The colors need to remain our blue and orange and the logo can not change. The squiggly lines have been used as our corporate identity for over 20 years and its time to update. Our company name is PELK (Bright Ledger Counter Solutions).

Target Market(s)

High End Jewelers

Industry/Entity Type

Software

Contact Information for Business Card

Requirements
Must have
• Our logo and the colors must remain the same. Blue is #d95d39 and Orange is #0f5682.
Nice to have
• The circle and arrow incorporated but not a requirement.
Should not have
• Anything jewelry or gem related.

```html
<!DOCTYPE html>
<html lang="en">
<head>
<meta charset="utf-8">
<title>PELK Business Card</title>
<link href="https://fonts.googleapis.com/css2?family=Open+Sans:wght@400;700&display=swap" rel="stylesheet">
<style>
  :root {
    --brand-blue: #0b5686;
    --brand-blue-light: #3fa0dc;
    --brand-orange: #d95d39;
    --ink-grey: #555b60;
    --paper: #ffffff;
    --backdrop: #2b2d30;
  }
  * { margin: 0; padding: 0; box-sizing: border-box; }
  html, body { width: 1200px; height: 900px; overflow: hidden; }
  body {
    background: var(--backdrop);
    font-family: "Open Sans", Arial, sans-serif;
    position: relative;
  }
  .card {
    position: absolute;
    left: 320px;
    width: 560px;
    height: 320px;
    overflow: hidden;
    box-shadow: 0 10px 30px rgba(0,0,0,.45);
  }
  .card--front { top: 70px; background: var(--paper); }
  .card--back { top: 470px; background: var(--brand-blue); }

  .person { position: absolute; left: 32px; top: 34px; }
  .person__name { font-size: 25px; font-weight: 700; color: var(--brand-blue); line-height: 1.1; }
  .person__title { font-size: 16px; color: var(--ink-grey); margin-top: 2px; }

  .divider {
    position: absolute; left: 32px; top: 104px;
    width: 470px; height: 1.5px; background: var(--brand-blue);
  }

  .contacts { position: absolute; left: 32px; top: 122px; list-style: none; }
  .contacts li {
    display: flex; align-items: center; gap: 8px;
    font-size: 15px; color: var(--ink-grey); line-height: 1.5;
  }
  .contacts svg { width: 12px; height: 12px; fill: var(--brand-orange); flex: none; }

  .company-name {
    position: absolute;
    font-weight: 700;
    color: var(--brand-blue);
    line-height: 1;
    letter-spacing: 2px;
  }
  .card--front .company-name { right: 40px; top: 44px; font-size: 40px; }

  .address {
    position: absolute; right: 40px; top: 196px;
    text-align: right; font-size: 15px; color: var(--ink-grey); line-height: 1.35;
  }

  .footer-bands { position: absolute; left: 0; bottom: 0; width: 560px; height: 60px; }
  .website {
    position: absolute; right: 40px; bottom: 7px;
    font-size: 15px; color: var(--paper);
  }

  .card--back .company-name {
    left: 50%; top: 50%; transform: translate(-50%, -50%);
    font-size: 72px; color: var(--paper); letter-spacing: 4px;
  }
</style>
</head>
<body>

<section class="card card--front" aria-label="Business card front">
  <div class="person">
    <div class="person__name">Dorian Vance</div>
    <div class="person__title">Director of Global Operations</div>
  </div>

  <div class="company-name">PELK</div>

  <div class="divider"></div>

  <ul class="contacts">
    <li>
      <svg viewBox="0 0 12 12" aria-hidden="true"><path d="M2.5 1l2 2-1 1.5c.6 1.5 1.8 2.7 3.3 3.3L8.3 6.8l2 2-1.2 2C5 10.5 1.5 7 1 3z"/></svg>
      +1-800-555-0148
    </li>
    <li>
      <svg viewBox="0 0 12 12" aria-hidden="true"><rect x="3" y="1" width="6" height="3"/><rect x="1" y="4.5" width="10" height="4.5" rx="1"/><rect x="3" y="8" width="6" height="3"/></svg>
      +1 702 555-0172
    </li>
    <li>
      <svg viewBox="0 0 12 12" aria-hidden="true"><path d="M1 3h10v6.5H1z M1 3l5 3.5L11 3"/></svg>
      dorian@pelkusa.com
    </li>
  </ul>

  <div class="address">
    1480 Harbor Plaza<br>
    Suite 210, Riverton,<br>
    NV 89000, USA
  </div>

  <svg class="footer-bands" viewBox="0 0 560 60" aria-hidden="true">
    <path d="M0 30 L300 48 L300 52 L0 34 Z" fill="var(--brand-orange)"/>
    <path d="M0 40 L300 52 C318 53 330 30 350 30 L560 30 L560 60 L0 60 Z" fill="var(--brand-blue)"/>
  </svg>
  <div class="website">www.pelkusa.com</div>
</section>

<section class="card card--back" aria-label="Business card back">
  <div class="company-name">PELK</div>
</section>

</body>
</html>
```